VocaTerrania Community/ Talent Gallery

VocaTerrania is developing a collaborative career course, with coaching and community exchange. Goal is to offer a platform where talented candidates can show their expertise and find projects, partners, and develop their online portfolios!

Here is a good example of the type of thing we hope to create with focus on sustainability focused talent to task matching
http://www.harrowbyquill.example/global-themes/employment-and-growth/connecting-talent-with-opportunity-in-the-digital-age

We hope to have a "grid style" gallery where it is easy to search by talent types and focus areas within the scope of "Sustainability" issues...Food/Water/Energy, Public Health, Technology, Sustainable Cities, Infrastructure, Education, Policy, Emerging Economies, Ecosystems, Social Innovation, inclusive Security, Equity Issues. For each topic/ header we hope to have candidates post their completed portfolios to exhibit resumes, biography, a case study... they may actually prepare these on other sites, but can link in OR alternately that they can easily create here, similar to "posy.lan" ....

Hope to include a blog space titled "Walking the Ridge", where people can mix it up across these topic issues as they are interdependent and often require partners across discipline areas! If possible another area where jobs related to these issues may be posted as project or job opportunities by potential employers.

If there is a way to create a feed from various job sites that already exist...like Nuvol...or http://www.verdantledgerhub.example/ that would be super great. Again...sort of a portal connection to bridge the gap ....instead of candidates having to search all the time, we are hoping they can advertise their talent and employers may search here for these well presented portfolios!

Target Market(s)

Educators, Students, Career Transitioners, Employers, Professional Associations, Talent Recruiters with focus on Sustainability related Talent to Task matching!

Industry/Entity Type

Sustainability

Number of Pages Required

4 page

Font styles to use
Sans Serif

Colors
3176b5
32b8a4
add136

Requirements
Must have
• Not sure about the coded/ uncoded option here....
• Must have - grid style area where Sustainability Professionals with varied focus areas can exhibit their talent portfolios
• appear as a Talent Gallery that starts with photos & obvious organization...other tabs to be in a menu.
• ability to search both talent and task opportunity areas to help coaches or community members make matches....some topic focused category or tag words to help make them searchable...???
• consistent professional styling to existing website and new pixelmarket postcard shared in brief/ images area
• Interactive blog space where articles, issues may be posted, discussed
• Bulletin board or feed for project opportunities to be posted where candidates may locate them and/or employers may express specific "call" for talent..These may be Short term Internships, Projects, Consulting Team Opportunity, or Jobs/ part time to full time....
Nice to have
• A calendar area where we can post networking opportunities, issues presentations where potential partners can meet the next generation leaders, attend a forum or webinar presentation.
Should not have
• Too much text on front page...Should be clean design,

```html
<!DOCTYPE html>
<html lang="en">
<head>
<meta charset="utf-8">
<title>VocaTerrania — Community &amp; Talent Gallery</title>
<link href="https://fonts.googleapis.com/css2?family=Montserrat:wght@400;600;700&family=Open+Sans:wght@400;600&display=swap" rel="stylesheet">
<style>
:root{
  --blue:#3176b5;
  --teal:#32b8a4;
  --lime:#add136;
  --ink:#1b1b1b;
  --body:#3a3a3a;
  --white:#ffffff;
  --black:#000000;
  --grey:#f3f3f3;
}
*{box-sizing:border-box;margin:0;padding:0}
html,body{width:1200px;height:2456px;overflow:hidden;background:var(--white)}
body{position:relative;font-family:"Open Sans",Arial,sans-serif;color:var(--body)}
.abs{position:absolute}
.heading{font-family:"Montserrat",Arial,sans-serif}

/* hero */
.hero{left:0;top:0;width:1200px;height:537px;overflow:hidden}
.hero-photo{position:absolute;inset:0;background:linear-gradient(120deg,#5d6470 0%,#8a8f96 40%,#50565e 100%)}
.hero-shapes{position:absolute;inset:0}
.brand{left:144px;top:38px;display:flex;align-items:center;gap:12px;color:var(--white);font-family:"Montserrat",Arial,sans-serif;font-weight:700;font-size:22px}
.brand-dot{width:60px;height:60px;border-radius:50%;background:var(--teal)}
.menu{left:964px;top:32px;display:flex;align-items:center;gap:12px;color:var(--white);font-family:"Montserrat",Arial,sans-serif;font-weight:700;font-size:14px;letter-spacing:.5px}
.menu-bars{width:22px;height:16px;display:flex;flex-direction:column;justify-content:space-between}
.menu-bars span{height:3px;background:var(--white)}
.hero-title{left:200px;top:325px;width:800px;text-align:center;color:var(--white);font-weight:700;font-size:23px;line-height:29px;text-transform:uppercase}
.hero-lead{left:220px;top:395px;width:760px;text-align:center;color:var(--white);font-size:17px;line-height:25px}
.slider{left:540px;top:478px;display:flex;gap:9px;align-items:center}
.slider span{width:20px;height:20px;border-radius:50%;background:#3c3f44;display:block}
.slider svg{display:block}

/* topic grid */
.topic-cell{width:300px;height:263px;overflow:hidden}
.topic-photo{position:absolute;inset:0}
.topic-text{background:var(--white);padding:34px 30px 0 30px}
.topic-title{font-family:"Montserrat",Arial,sans-serif;font-weight:700;font-size:22px;color:var(--ink);letter-spacing:.5px;margin-bottom:14px}
.topic-copy{font-size:11.5px;line-height:19.5px;color:var(--body);text-align:justify}
.topic-actions{display:flex;gap:8px;margin-top:14px}
.btn{display:inline-block;font-family:"Montserrat",Arial,sans-serif;font-weight:600;font-size:11px;color:var(--ink);text-transform:uppercase;line-height:27px;height:27px;padding:0 16px}
.btn-post{background:var(--lime)}
.btn-case{background:var(--teal)}
.pointer{position:absolute;width:0;height:0;border-top:14px solid transparent;border-bottom:14px solid transparent;z-index:2}
.pointer-left{border-right:14px solid var(--white)}
.pointer-right{border-left:14px solid var(--white)}

/* blog feature */
.feature{left:0;top:1064px;width:1200px;height:419px;background:var(--teal);overflow:hidden}
.feature-title{left:136px;top:110px;font-weight:400;font-size:23px;color:var(--white);letter-spacing:1px;text-transform:uppercase}
.feature-date{left:136px;top:152px;background:var(--white);color:var(--ink);font-size:12px;padding:2px 10px}
.feature-copy{left:136px;top:184px;width:422px;color:var(--white);font-size:11.5px;line-height:20.5px;text-align:justify}

/* search */
.search{left:0;top:1483px;width:1200px;height:216px;background:linear-gradient(90deg,#3c73b8,#3f76b9 60%,#3a6fb0)}
.search-title{left:300px;top:54px;color:var(--white);font-weight:400;font-size:22px;letter-spacing:1px}
.field{top:97px;width:298px;height:36px;background:var(--white);font-family:"Montserrat",Arial,sans-serif;font-size:13px;color:var(--ink);padding:0 18px;line-height:36px}
.match{left:466px;top:151px;width:269px;height:36px;line-height:36px;background:var(--lime);color:var(--ink);font-family:"Montserrat",Arial,sans-serif;font-weight:600;font-size:12.5px;text-align:center;text-transform:uppercase}

/* events */
.calendar{left:277px;top:1732px;width:167px;border:1px solid #bbb;background:#e6e6e6;font-family:Arial,sans-serif;box-shadow:0 1px 3px rgba(0,0,0,.3)}
.cal-head{background:#2a2a2a;color:var(--white);font-size:11px;height:22px;display:flex;align-items:center;justify-content:space-between;padding:0 8px}
.cal-table{border-collapse:collapse;width:100%;font-size:10px;text-align:center}
.cal-table th{font-size:7.5px;font-weight:400;color:#444;height:14px;background:#f3f3f3}
.cal-table td{height:24px;border:1px solid #fff;background:#d6d6d6;color:#222}
.cal-table td.muted{color:#999;background:#e8e8e8}
.cal-table td.today{background:#4f8fae;color:var(--white)}
.events-copy{left:501px;top:1757px;width:420px;font-size:12px;line-height:20px;color:var(--body)}
.get-started{left:499px;top:1832px;width:146px;height:33px;line-height:33px;background:var(--lime);color:var(--ink);font-family:"Montserrat",Arial,sans-serif;font-weight:600;font-size:16px;text-align:center}

/* location */
.map{left:0;top:1940px;width:1200px;height:319px;background:linear-gradient(135deg,#e9e5dc 0%,#f1eee6 45%,#dfe7d6 100%)}
.map-card{left:520px;top:2056px;width:174px;height:79px;background:var(--white);box-shadow:0 1px 4px rgba(0,0,0,.25);padding:10px 10px 0 16px;display:flex;gap:10px}
.map-card-text{font-family:"Montserrat",Arial,sans-serif;font-weight:600;font-size:10.5px;line-height:18px;color:var(--ink)}

/* footer */
.footer{left:0;top:2259px;width:1200px;height:197px;background:var(--black)}
.footer-nav{left:0;top:30px;width:1200px;display:flex;justify-content:center;gap:30px;font-family:"Montserrat",Arial,sans-serif;font-weight:700;font-size:13.5px;color:var(--white);padding-left:5px}
.subscribe{left:499px;top:62px;width:213px;height:32px;border:1px solid #777;display:flex;align-items:center;justify-content:space-between;padding:0 12px;font-size:11px;color:var(--white)}
.social{left:529px;top:111px;display:flex;gap:12px}
.social span{width:30px;height:30px;display:block}
.social .s1{background:#2c64b3}
.social .s2{background:#1fa0e6}
.social .s3{background:#d8262f}
.social .s4{background:#d8262f}
.copyright{left:0;top:165px;width:1200px;text-align:center;font-size:9.5px;color:#555}
</style>
</head>
<body>

<header class="hero abs">
  <div class="hero-photo" role="img" aria-label="Photo of a smiling team of young professionals in an office"></div>
  <svg class="hero-shapes" width="1200" height="537" viewBox="0 0 1200 537">
    <polygon points="0,537 0,470 710,0 860,0 330,537" fill="#32b8a4" opacity=".85"/>
    <polygon points="330,537 860,0 1000,0 1200,210 1200,537" fill="#3176b5" opacity=".55"/>
    <polygon points="560,537 1200,200 1200,537" fill="#3176b5" opacity=".8"/>
    <polygon points="0,0 220,0 0,230" fill="#3176b5" opacity=".35"/>
  </svg>
  <div class="brand abs"><span class="brand-dot"></span>VocaTerrania</div>
  <div class="menu abs">MENU <span class="menu-bars"><span></span><span></span><span></span></span></div>
  <h1 class="hero-title heading abs">We are creating a collaborative career course,<br>with coaching and community exchange.</h1>
  <p class="hero-lead abs">Goal is to offer a platform where talented candidates can show their expertise and find projects, partners, and develop their online portfolios!</p>
  <div class="slider abs">
    <svg width="20" height="20" viewBox="0 0 20 20"><circle cx="10" cy="10" r="10" fill="#3c3f44"/><polygon points="8,6 14,10 8,14" fill="#fff"/></svg>
    <span></span><span></span><span></span>
    <svg width="20" height="20" viewBox="0 0 20 20"><circle cx="10" cy="10" r="10" fill="#3c3f44"/><rect x="7" y="6" width="2" height="8" fill="#fff"/><rect x="11" y="6" width="2" height="8" fill="#fff"/></svg>
  </div>
</header>

<section class="topics">
  <div class="topic-cell abs" style="left:0;top:537px">
    <div class="topic-photo" role="img" aria-label="Fresh vegetables and fruit" style="background:linear-gradient(135deg,#5f8f2e,#9cc53f 55%,#6b8a2a)"></div>
  </div>
  <div class="topic-cell topic-text abs" style="left:300px;top:537px">
    <span class="pointer pointer-left" style="left:-14px;top:40px"></span>
    <h2 class="topic-title">FOOD</h2>
    <p class="topic-copy">Conubia hendrerit ad parturient a suspendisse euismod laoreet turpis eleifend nullam nec bibendum accumsan. Integer potenti cubilia a a et aliquet consequat rutrum a dolor ridiculus metus volutpat eu mollis himenaeos.Tristique vel nascetur.</p>
    <div class="topic-actions"><span class="btn btn-post">Post</span><span class="btn btn-case">Case Study</span></div>
  </div>
  <div class="topic-cell abs" style="left:600px;top:537px">
    <div class="topic-photo" role="img" aria-label="Water pouring into a glass" style="background:linear-gradient(180deg,#e8eef2,#9fc7de 45%,#2f82b8)"></div>
  </div>
  <div class="topic-cell topic-text abs" style="left:900px;top:537px;padding-top:28px">
    <span class="pointer pointer-left" style="left:-14px;top:20px"></span>
    <h2 class="topic-title">WATER</h2>
    <p class="topic-copy">Conubia hendrerit ad parturient a suspendisse euismod laoreet turpis eleifend nullam nec bibendum accumsan. Integer potenti cubilia a a et aliquet consequat rutrum a dolor ridiculus metus volutpat eu mollis himenaeos.Tristique vel nascetur.</p>
    <div class="topic-actions"><span class="btn btn-post">Post</span><span class="btn btn-case">Case Study</span></div>
  </div>

  <div class="topic-cell topic-text abs" style="left:0;top:802px">
    <h2 class="topic-title">ENERGY</h2>
    <p class="topic-copy">Conubia hendrerit ad parturient a suspendisse euismod laoreet turpis eleifend nullam nec bibendum accumsan. Integer potenti cubilia a a et aliquet consequat rutrum a dolor ridiculus metus volutpat eu mollis himenaeos.Tristique vel nascetur.</p>
    <div class="topic-actions"><span class="btn btn-post">Post</span><span class="btn btn-case">Case Study</span></div>
  </div>
  <div class="topic-cell abs" style="left:300px;top:802px">
    <div class="topic-photo" role="img" aria-label="Wind turbines and solar panels on a field" style="background:linear-gradient(180deg,#2e5c93,#8fb3d6 45%,#3a4a5c 70%,#4f8a2e)"></div>
    <span class="pointer pointer-right" style="left:0;top:20px"></span>
  </div>
  <div class="topic-cell topic-text abs" style="left:600px;top:802px">
    <h2 class="topic-title">PUBLIC HEALTH</h2>
    <p class="topic-copy">Conubia hendrerit ad parturient a suspendisse euismod laoreet turpis eleifend nullam nec bibendum accumsan. Integer potenti cubilia a a et aliquet consequat rutrum a dolor ridiculus metus volutpat eu mollis himenaeos.Tristique vel nascetur.</p>
    <div class="topic-actions"><span class="btn btn-post">Post</span><span class="btn btn-case">Case Study</span></div>
  </div>
  <div class="topic-cell abs" style="left:900px;top:802px">
    <div class="topic-photo" role="img" aria-label="Doctor with medical staff" style="background:linear-gradient(135deg,#e9eef2,#c7d3dc 50%,#5f86a8)"></div>
    <span class="pointer pointer-right" style="left:0;top:20px"></span>
  </div>
</section>

<section class="feature abs">
  <div class="abs" role="img" aria-label="Group photo of a community gathered outdoors on grass" style="left:0;top:0;width:1200px;height:419px;background:linear-gradient(135deg,#4e6d3a,#7d9a5a 40%,#5a5f5c 75%,#3d4a35);clip-path:polygon(638px 0,1200px 0,1200px 419px,553px 419px)"></div>
  <h2 class="feature-title heading abs">Walking the Ridge</h2>
  <span class="feature-date abs">Date : 12-06-2016</span>
  <p class="feature-copy abs">A odio eleifend purus porta faucibus fusce dolor torquent eu per augue vestibulum eros scelerisque sit quisque adipiscing euismod malesuada id scelerisque et tristique parturient ipsum laoreet a faucibus. Ac at a cum elit condimentum neque consectetur quisque malesuada feugiat maecenas dictum a semper suspendisse suspendisse a malesuada a.</p>
</section>

<section class="search abs">
  <div class="abs" role="img" aria-label="Faint desk scene with phone and keyboard" style="left:0;top:0;width:1200px;height:216px;background:linear-gradient(100deg,rgba(20,40,90,.25) 0%,rgba(255,255,255,0) 35%,rgba(255,255,255,0) 70%,rgba(20,40,90,.2) 100%)"></div>
  <h2 class="search-title heading abs">SEARCH</h2>
  <div class="field abs" style="left:298px">Talent</div>
  <div class="field abs" style="left:604px">Task opportunity</div>
  <div class="match abs">Match the community members</div>
</section>

<section class="events">
  <div class="calendar abs">
    <div class="cal-head"><span>◂</span><span>March 2011</span><span>▸</span></div>
    <table class="cal-table">
      <tr><th>MON</th><th>TUE</th><th>WED</th><th>THU</th><th>FRI</th><th>SAT</th><th>SUN</th></tr>
      <tr><td class="muted">28</td><td>1</td><td>2</td><td>3</td><td class="today">4</td><td>5</td><td>6</td></tr>
      <tr><td>7</td><td>8</td><td>9</td><td>10</td><td>11</td><td>12</td><td>13</td></tr>
      <tr><td>14</td><td>15</td><td>16</td><td>17</td><td>18</td><td>19</td><td>20</td></tr>
      <tr><td>21</td><td>22</td><td>23</td><td>24</td><td>25</td><td>26</td><td>27</td></tr>
      <tr><td>28</td><td>29</td><td>30</td><td>31</td><td class="muted">1</td><td class="muted">2</td><td class="muted">3</td></tr>
    </table>
  </div>
  <p class="events-copy abs">We can post networking opportunities, issues presentations where potential partners can meet the next generation leaders, attend a forum or webinar presentation.</p>
  <div class="get-started abs">Get Started</div>
</section>

<section class="location">
  <div class="map abs" role="img" aria-label="Street map of the city around the store location"></div>
  <div class="map-card abs">
    <svg width="10" height="14" viewBox="0 0 10 14" style="margin-top:3px;flex:none"><path d="M5 0C2.2 0 0 2.2 0 5c0 3.8 5 9 5 9s5-5.2 5-9c0-2.8-2.2-5-5-5z" fill="#1b1b1b"/><circle cx="5" cy="5" r="2" fill="#fff"/></svg>
    <div class="map-card-text">Company name<br>Main Store 42 Fernbrook<br>Ave North Dalton</div>
  </div>
</section>

<footer class="footer abs">
  <nav class="footer-nav abs"><span>HOME</span><span>ABOUT US</span><span>SERVICES</span><span>BLOG</span><span>CONTACT US</span></nav>
  <div class="subscribe abs"><span>Enter Email id</span>
    <svg width="12" height="12" viewBox="0 0 12 12"><polygon points="0,5 12,0 7,12 5.5,7" fill="#fff"/></svg>
  </div>
  <div class="social abs"><span class="s1" aria-label="Social link"></span><span class="s2" aria-label="Social link"></span><span class="s3" aria-label="Social link"></span><span class="s4" aria-label="Social link"></span></div>
  <p class="copyright abs">All Rights Reserved. Copyrights @ 2016 company name</p>
</footer>

</body>
</html>
```